SEO Company Needs a Professional, Bold Business Card Design

Kelvo SEO
2487 N Harlow Ave #315
Austin, TX 78799
512-555-0184
http://www.kelvoseo-demo.com
Kelvo SEO is an internet marketing company specializing in SEO for higher-end businesses. We are looking for a professional and bold (edgy) design that communicates our forward thinking SEO strategies. Our typical client is a small to medium US business that has never had SEO work done on their website but does has active marketing. We want our business card design to instill confidence in our services through a professional and bold look. We we would also like the design elements to be in line with the services we offer - ranking client websites in the search engine results, namely Zarnix.
Design Specifics:
Card design should have square edges.
Design should be delivered in fully layered and editable PSD file. Designing in AI is fine but I need a PSD file in case we have any changes in contact information or need additional cards for employees.
The design should compliment the attached logo.
Company Name:
Kelvo SEO
Address:
2487 N Harlow Ave #315
Austin, TX 78799
Personal Info:
Dorian Welk
Owner
dwelk@kelvoseo-demo.com
Phone:
877-555-0139 (KELVO UP)
Website:
http://www.kelvoseo-demo.com
Slogan:
Could Your Website Be Generating More Business?
Target Market(s)
High-end business owners - doctors, lawyers, specialists, business owners doing 250k in profit.
Industry/Entity Type
Internet
Contact Information for Business Card
Company Name:
Kelvo SEO
Address:
640 Larkfield Dr Ste 208
Austin, TX 78799
Personal Info:
Dorian Welk
Owner
dwelk@kelvoseo-demo.com
Phone:
877-555-0139 (KELVO UP)
Website:
www.kelvoseo-demo.com
Slogan:
Requirements
Must have
- Card design should have square edges.
- Background should be WHITE only.
- Design should be delivered in fully layered and editable PSD file. Designing in AI is fine but I need a PSD file in case we have any changes in contact information or need additional cards for employees.

```html
<!DOCTYPE html>
<html lang="en">
<head>
<meta charset="utf-8">
<title>Kelvo SEO Business Card</title>
<link href="https://fonts.googleapis.com/css2?family=Open+Sans:wght@400;600;700&family=Oswald:wght@400;500&display=swap" rel="stylesheet">
<style>
  :root {
    --stage: #e6e4e2;
    --card: #ffffff;
    --navy: #1d2f4f;
    --blue: #1ca0e0;
    --ink: #4a4a4a;
    --rule: #2b3d5c;
  }
  * { box-sizing: border-box; margin: 0; padding: 0; }
  html, body { width: 1200px; height: 716px; overflow: hidden; }
  body {
    background: var(--stage);
    font-family: "Open Sans", sans-serif;
    position: relative;
  }
  .card {
    position: absolute;
    top: 200px;
    width: 540px;
    height: 309px;
    background: var(--card);
    box-shadow: 0 6px 18px rgba(0,0,0,0.18);
  }
  .card-front { left: 40px; }
  .card-back { left: 620px; }

  .brand {
    display: flex;
    align-items: center;
    gap: 10px;
    color: var(--navy);
    font-family: "Open Sans", sans-serif;
    font-weight: 700;
    white-space: nowrap;
  }
  .brand-dot {
    border-radius: 50%;
    background: var(--navy);
    flex: none;
  }
  .card-front .brand {
    position: absolute;
    left: 50%;
    top: 50%;
    transform: translate(-50%, -50%);
    font-size: 40px;
  }
  .card-front .brand-dot { width: 30px; height: 30px; }

  .card-back .brand {
    position: absolute;
    left: 34px;
    top: 110px;
    font-size: 30px;
  }
  .card-back .brand-dot { width: 22px; height: 22px; }

  .slogan {
    position: absolute;
    left: 34px;
    top: 162px;
    width: 230px;
    padding-top: 8px;
    border-top: 1.5px solid var(--rule);
    font-family: "Oswald", sans-serif;
    font-weight: 500;
    font-size: 17px;
    line-height: 1.15;
    text-transform: uppercase;
    color: var(--navy);
  }

  .person {
    position: absolute;
    right: 60px;
    top: 48px;
    text-align: left;
  }
  .person-name { color: var(--blue); font-weight: 600; font-size: 17px; }
  .person-role { color: var(--ink); font-size: 15px; margin-top: -2px; }

  .contact-list {
    position: absolute;
    left: 300px;
    top: 170px;
    list-style: none;
    color: var(--ink);
    font-size: 14px;
    line-height: 1.35;
  }
  .contact-list li { display: flex; align-items: flex-start; gap: 7px; }
  .contact-list svg { width: 11px; height: 11px; margin-top: 4px; flex: none; fill: var(--blue); }
</style>
</head>
<body>

  <section class="card card-front" aria-label="Card front">
    <div class="brand"><span class="brand-dot"></span>Kelvo SEO</div>
  </section>

  <section class="card card-back" aria-label="Card back">
    <div class="brand"><span class="brand-dot"></span>Kelvo SEO</div>
    <p class="slogan">Could your website be<br>generating more business?</p>

    <div class="person">
      <p class="person-name">Dorian Welk</p>
      <p class="person-role">Owner</p>
    </div>

    <ul class="contact-list">
      <li>
        <svg viewBox="0 0 24 24" aria-hidden="true"><path d="M6.6 10.8a15.1 15.1 0 0 0 6.6 6.6l2.2-2.2a1 1 0 0 1 1-.25 11.4 11.4 0 0 0 3.6.57 1 1 0 0 1 1 1V20a1 1 0 0 1-1 1A17 17 0 0 1 3 4a1 1 0 0 1 1-1h3.5a1 1 0 0 1 1 1c0 1.250.2 2.45.57 3.6a1 1 0 0 1-.25 1z"/></svg>
        <span>877-555-0139 (KELVO UP)</span>
      </li>
      <li>
        <svg viewBox="0 0 24 24" aria-hidden="true"><path d="M12 2a10 10 0 1 0 5 18.7l-1-1.7A8 8 0 1 1 20 12v1a2 2 0 0 1-4 0V7h-2v1a5 5 0 1 0 .7 6.6A4 4 0 0 0 22 13v-1A10 10 0 0 0 12 2zm0 13a3 3 0 1 1 0-6 3 3 0 0 1 0 6z"/></svg>
        <span>dwelk@kelvoseo-demo.com</span>
      </li>
      <li>
        <svg viewBox="0 0 24 24" aria-hidden="true"><path d="M10.6 13.4a1 1 0 0 1 0-1.4l3.5-3.5a1 1 0 1 1 1.4 1.4L12 13.4a1 1 0 0 1-1.4 0zM8 20a4 4 0 0 1-2.8-6.8l2.5-2.5 1.4 1.4-2.5 2.5a2 2 0 1 0 2.8 2.8l2.5-2.5 1.4 1.4-2.5 2.5A4 4 0 0 1 8 20zm8.3-6.7-1.4-1.4 2.5-2.5a2 2 0 1 0-2.8-2.8l-2.5 2.5-1.4-1.4 2.5-2.5a4 4 0 1 1 5.6 5.6z"/></svg>
        <span>www.kelvoseo-demo.com</span>
      </li>
      <li>
        <svg viewBox="0 0 24 24" aria-hidden="true"><path d="M12 2a7 7 0 0 0-7 7c0 5.2 7 13 7 13s7-7.8 7-13a7 7 0 0 0-7-7zm0 9.5A2.5 2.5 0 1 1 12 6.5a2.5 2.5 0 0 1 0 5z"/></svg>
        <span>640 Larkfield Dr Ste 208<br>Austin, TX 78799</span>
      </li>
    </ul>
  </section>

</body>
</html>
```